Flex Forward Thaw 21 day Challenge

We are having a Flex Forward Thaw Challenge at our fitness studio. We need a poster design using the template attached as a reference. I have also included our Molvaro logo to put on the poster. Please DO NOT use the graphics in the flyer as we are expecting something much better :-)

-Size needed 11x17 with bleeding for printing

-We need this made in Photoshop (CS3 friendly) or at least delivered in PS as we might change some text or re-arrange the design later on.

-We need this in layers.

```html
<!DOCTYPE html>
<html lang="en">
<head>
<meta charset="utf-8">
<title>Flex Forward Thaw 21 Day Challenge Poster</title>
<link rel="stylesheet" href="https://fonts.googleapis.com/css2?family=Oswald:wght@500;700&family=Arimo:wght@400&family=Share+Tech+Mono&display=swap">
<style>
  :root {
    --page-bg: #ffffff;
    --sky-top: #7fb0de;
    --sky-low: #a9c9e6;
    --sea: #2f5f92;
    --sand-top: #a97a45;
    --sand-mid: #7a4423;
    --earth-deep: #3a1206;
    --gold: #d49a4e;
    --gold-light: #f3d68e;
    --red-dark: #5e0b0d;
    --red-bright: #d9232b;
    --white: #ffffff;
    --ink: #262626;
  }
  html, body {
    margin: 0;
    width: 1000px;
    height: 1200px;
    overflow: hidden;
    background: var(--page-bg);
  }
  .poster {
    position: absolute;
    left: 163px;
    top: 83px;
    width: 675px;
    height: 1035px;
    overflow: hidden;
  }
  .poster svg { display: block; width: 675px; height: 1035px; }
  .display { font-family: "Oswald", "Arial Narrow", sans-serif; font-weight: 700; }
  .body-copy { font-family: "Arimo", Arial, sans-serif; font-size: 15px; fill: var(--white); }
  .quote { font-family: "Share Tech Mono", "Courier New", monospace; font-size: 15px; fill: var(--white); }
  .brand-name { font-family: "Oswald", "Arial Narrow", sans-serif; font-weight: 700; fill: var(--ink); letter-spacing: 3px; }
  .web { font-family: "Arimo", Arial, sans-serif; font-size: 13px; fill: var(--white); }
</style>
</head>
<body>
<div class="poster">
  <svg viewBox="0 0 675 1035" xmlns="http://www.w3.org/2000/svg">
    <defs>
      <linearGradient id="sky" x1="0" y1="0" x2="0" y2="1">
        <stop offset="0" stop-color="var(--sky-top)"/>
        <stop offset="0.66" stop-color="var(--sky-low)"/>
        <stop offset="0.7" stop-color="var(--sea)"/>
        <stop offset="1" stop-color="#284f7d"/>
      </linearGradient>
      <linearGradient id="earth" x1="0" y1="0" x2="0" y2="1">
        <stop offset="0" stop-color="var(--sand-top)"/>
        <stop offset="0.35" stop-color="var(--sand-mid)"/>
        <stop offset="1" stop-color="var(--earth-deep)"/>
      </linearGradient>
      <linearGradient id="headline-red" x1="0" y1="0" x2="1" y2="0">
        <stop offset="0" stop-color="var(--red-dark)"/>
        <stop offset="0.6" stop-color="var(--red-bright)"/>
        <stop offset="1" stop-color="var(--red-dark)"/>
      </linearGradient>
      <linearGradient id="headline-gold" x1="0" y1="0" x2="0" y2="1">
        <stop offset="0" stop-color="var(--gold-light)"/>
        <stop offset="1" stop-color="var(--gold)"/>
      </linearGradient>
      <linearGradient id="quote-pill" x1="0" y1="0" x2="1" y2="0">
        <stop offset="0" stop-color="var(--red-dark)"/>
        <stop offset="0.5" stop-color="var(--red-bright)"/>
        <stop offset="1" stop-color="var(--red-dark)"/>
      </linearGradient>
    </defs>

    <!-- hero photo area -->
    <rect class="hero-photo" x="0" y="0" width="675" height="545" fill="url(#sky)" role="img" aria-label="Photo of a fit woman in a white sports bra measuring her waist with a tape, beach sky and sea behind"/>

    <!-- sand ground and lower panel -->
    <path class="ground" d="M0,522 Q180,500 360,514 T675,502 L675,1035 L0,1035 Z" fill="url(#earth)"/>

    <!-- brand -->
    <text class="brand-name" x="489" y="112" font-size="54" text-anchor="middle">MOLVARO</text>

    <!-- headline -->
    <g class="headline display">
      <text x="334" y="287" font-size="80" textLength="311" lengthAdjust="spacingAndGlyphs" fill="url(#headline-red)">FLEX</text>
      <text x="334" y="407" font-size="146" textLength="311" lengthAdjust="spacingAndGlyphs" fill="url(#headline-gold)">FORWARD</text>
      <text x="334" y="527" font-size="152" textLength="311" lengthAdjust="spacingAndGlyphs" fill="url(#headline-red)">THAW</text>
    </g>

    <!-- tagline -->
    <g class="tagline display" fill="var(--white)">
      <text x="30" y="582" font-size="27" textLength="239" lengthAdjust="spacingAndGlyphs">DISCOVER THE SECRET TO</text>
      <text x="30" y="617" font-size="27" textLength="239" lengthAdjust="spacingAndGlyphs">A BEACH-READY BODY</text>
      <text x="280" y="622" font-size="70" textLength="365" lengthAdjust="spacingAndGlyphs">IN JUST 21 DAYS!</text>
    </g>

    <!-- benefit list -->
    <g class="benefits">
      <g class="tick-box" fill="var(--gold)" stroke="var(--white)" stroke-width="2" stroke-linecap="round" stroke-linejoin="round">
        <rect x="32" y="657" width="14" height="14" stroke="none"/>
        <path d="M35,664 l3,4 l7,-9" fill="none"/>
        <rect x="32" y="701" width="14" height="14" stroke="none"/>
        <path d="M35,708 l3,4 l7,-9" fill="none"/>
        <rect x="32" y="745" width="14" height="14" stroke="none"/>
        <path d="M35,752 l3,4 l7,-9" fill="none"/>
        <rect x="32" y="789" width="14" height="14" stroke="none"/>
        <path d="M35,796 l3,4 l7,-9" fill="none"/>
      </g>
      <text class="body-copy" x="57" y="670">9 total training sessions designed to incinerate</text>
      <text class="body-copy" x="57" y="692">fat off your midsection, thighs, and arms</text>
      <text class="body-copy" x="57" y="714">21 days of nutritional guidance, including</text>
      <text class="body-copy" x="57" y="736">delicious recipes</text>
      <text class="body-copy" x="57" y="758">A Success Session to map out your</text>
      <text class="body-copy" x="57" y="780">individual plan for success</text>
      <text class="body-copy" x="57" y="802">Your very own Personal Accountability Coach</text>
      <text class="body-copy" x="57" y="824">to ensure you get results</text>
    </g>

    <!-- price box -->
    <g class="offer display">
      <rect x="412" y="660" width="257" height="164" rx="6" fill="none" stroke="var(--gold)" stroke-width="2"/>
      <text x="540" y="711" font-size="33" text-anchor="middle" fill="var(--white)" font-weight="500">YOU GET ALL THIS</text>
      <text x="540" y="746" font-size="26" text-anchor="middle" fill="var(--white)" font-weight="500">— a $399 value —</text>
      <text x="438" y="800" font-size="42" textLength="205" lengthAdjust="spacingAndGlyphs" fill="var(--gold)" font-weight="500">for ONLY $99!</text>
    </g>

    <!-- testimonial -->
    <g class="testimonial">
      <rect x="32" y="847" width="637" height="36" rx="18" fill="url(#quote-pill)"/>
      <text class="quote" x="350" y="871" text-anchor="middle">"I've never been more fit in my life at age 41!" ~Dana Whitfield</text>
    </g>

    <!-- call to action -->
    <g class="cta display" fill="var(--gold)">
      <text x="30" y="932" font-size="40" textLength="615" lengthAdjust="spacingAndGlyphs" font-weight="500">HURRY! SPACE IS LIMITED TO ONLY 20 PARTICIPANTS!!!</text>
      <text x="30" y="987" font-size="52" textLength="345" lengthAdjust="spacingAndGlyphs" font-weight="500">CLAIM YOUR SPOT NOW</text>
      <g class="phone-icon" fill="none" stroke="var(--gold)" stroke-width="2.5">
        <circle cx="398" cy="967" r="15"/>
        <path d="M391,960 q0,-3 3,-3 l2,4 -2,2 q2,5 6,7 l2,-2 4,2 q0,3 -3,3 q-12,-3 -12,-13 z" fill="var(--gold)" stroke="none"/>
      </g>
      <text x="425" y="987" font-size="52" textLength="220" lengthAdjust="spacingAndGlyphs" font-weight="500">303-555-0148</text>
    </g>

    <g class="footer">
      <line x1="30" y1="999" x2="262" y2="999" stroke="#6a3a22" stroke-width="1"/>
      <line x1="414" y1="999" x2="645" y2="999" stroke="#6a3a22" stroke-width="1"/>
      <text class="web" x="338" y="1004" text-anchor="middle">www.molvaro.com</text>
    </g>
  </svg>
</div>
</body>
</html>
```